K7R Business Cards

Business Cards

Contact Information for Business Card

Company name, owner name, license #s, phone & email

Requirements
Should not have
• mailing address

```html
<!DOCTYPE html>
<html lang="en">
<head>
<meta charset="utf-8">
<title>K7R Business Cards</title>
<link rel="stylesheet" href="https://fonts.googleapis.com/css2?family=Open+Sans:wght@400;700;800&display=swap">
<style>
  :root {
    --backdrop: #cbcbcb;
    --card: #ffffff;
    --brand-blue: #233f94;
    --brand-red: #c1272d;
    --ink: #111111;
    --photo-dark: #050505;
    --photo-mid: #1d1d1f;
  }
  * { box-sizing: border-box; margin: 0; padding: 0; }
  html, body { width: 1200px; height: 780px; overflow: hidden; }
  body {
    background: var(--backdrop);
    font-family: "Open Sans", Arial, sans-serif;
    position: relative;
  }
  .card {
    position: absolute;
    left: 320px;
    width: 561px;
    height: 321px;
    background: var(--card);
    box-shadow: 0 4px 10px rgba(0,0,0,0.35);
    overflow: hidden;
  }
  .card--construction { top: 53px; }
  .card--realty { top: 406px; }

  .brand-name {
    position: absolute;
    color: var(--brand-blue);
    font-weight: 800;
    line-height: 1;
    letter-spacing: 2px;
  }
  .brand-division {
    position: absolute;
    color: var(--ink);
    font-weight: 700;
    line-height: 1;
  }
  .card--construction .brand-name { left: 0; width: 561px; text-align: center; top: 42px; font-size: 72px; }
  .card--construction .brand-division { left: 0; width: 561px; text-align: center; top: 117px; font-size: 31px; letter-spacing: 0.5px; }

  .owner-name {
    position: absolute;
    color: var(--brand-blue);
    font-weight: 700;
    font-size: 32px;
    line-height: 1;
    white-space: nowrap;
  }
  .license {
    position: absolute;
    color: var(--brand-red);
    font-size: 17.5px;
    line-height: 1;
    white-space: nowrap;
  }
  .card--construction .owner-name { right: 316px; top: 218px; }
  .card--construction .license { right: 316px; top: 253px; }
  .divider {
    position: absolute;
    left: 280px;
    top: 202px;
    width: 1.2px;
    height: 90px;
    background: var(--ink);
  }

  .contact-list { position: absolute; list-style: none; }
  .contact-item {
    display: flex;
    align-items: center;
    gap: 8px;
    font-size: 15.5px;
    color: var(--ink);
    line-height: 19px;
    white-space: nowrap;
  }
  .contact-icon { width: 13px; height: 13px; flex: none; }
  .card--construction .contact-list { left: 320px; top: 226px; }

  .card--realty .brand-name { left: 23px; width: 211px; text-align: center; top: 12px; font-size: 62px; }
  .card--realty .brand-division { left: 23px; width: 211px; text-align: center; top: 77px; font-size: 34px; }
  .name-marker {
    position: absolute;
    left: 0; top: 177px;
    width: 18px; height: 28px;
    background: var(--brand-red);
  }
  .card--realty .owner-name { left: 22px; top: 174px; }
  .card--realty .contact-list { left: 23px; top: 264px; }

  .portrait-panel { position: absolute; inset: 0; }
</style>
</head>
<body>

<section class="card card--construction">
  <div class="brand-name">K7R</div>
  <div class="brand-division">CONSTRUCTION</div>
  <div class="owner-name">Dean Harlow</div>
  <div class="license">MN License # BC482917</div>
  <div class="divider"></div>
  <ul class="contact-list">
    <li class="contact-item">
      <svg class="contact-icon" viewBox="0 0 16 16"><path fill="#c1272d" d="M3.5 1.5l2.4 0.3 1 3.2-1.6 1.3c0.8 1.7 2 2.9 3.6 3.7l1.3-1.6 3.2 1 0.3 2.4c-0.3 1.3-1.6 2.3-3 2.1C6.2 13.4 2.6 9.8 1.5 5.3 1.3 3.9 2.2 1.8 3.5 1.5z"/></svg>
      <span>555-014-2290</span>
    </li>
    <li class="contact-item">
      <svg class="contact-icon" viewBox="0 0 16 16"><path fill="#233f94" d="M1 6l7-5 7 5v9H1z"/><path fill="#fff" d="M3 7l5 4 5-4v6H3z"/><circle cx="8" cy="6.5" r="2" fill="none" stroke="#fff" stroke-width="1"/></svg>
      <span>Jdeanharlow@inbox.com</span>
    </li>
  </ul>
</section>

<section class="card card--realty">
  <svg class="portrait-panel" viewBox="0 0 561 321" width="561" height="321">
    <defs>
      <radialGradient id="portrait-tone" cx="0.62" cy="0.55" r="0.6">
        <stop offset="0" stop-color="var(--photo-mid)"/>
        <stop offset="1" stop-color="var(--photo-dark)"/>
      </radialGradient>
    </defs>
    <path d="M289 321 C272 270 268 200 284 140 C302 75 330 30 362 0 H561 V321 Z" fill="#000"/>
    <path role="img" aria-label="Portrait photo of the agent in a dark suit and tie on a black backdrop" fill="url(#portrait-tone)"
          d="M381 0 C322 55 286 150 300 235 C304 270 310 300 316 321 H561 V0 Z"/>
    <path d="M352 0 H381 C336 48 306 125 308 224 C296 150 312 62 352 0 Z" fill="#c1272d"/>
    <path d="M290 132 C279 205 294 275 308 321 H334 C311 280 294 215 290 132 Z" fill="#233f94"/>
  </svg>
  <div class="brand-name">K7R</div>
  <div class="brand-division">REALTY</div>
  <div class="name-marker"></div>
  <div class="owner-name">Dean Harlow</div>
  <ul class="contact-list">
    <li class="contact-item">
      <svg class="contact-icon" viewBox="0 0 16 16"><path fill="#c1272d" d="M3.5 1.5l2.4 0.3 1 3.2-1.6 1.3c0.8 1.7 2 2.9 3.6 3.7l1.3-1.6 3.2 1 0.3 2.4c-0.3 1.3-1.6 2.3-3 2.1C6.2 13.4 2.6 9.8 1.5 5.3 1.3 3.9 2.2 1.8 3.5 1.5z"/></svg>
      <span>555-014-2290</span>
    </li>
    <li class="contact-item">
      <svg class="contact-icon" viewBox="0 0 16 16"><path fill="#233f94" d="M1 6l7-5 7 5v9H1z"/><path fill="#fff" d="M3 7l5 4 5-4v6H3z"/><circle cx="8" cy="6.5" r="2" fill="none" stroke="#fff" stroke-width="1"/></svg>
      <span>Jdeanharlow@inbox.com</span>
    </li>
  </ul>
</section>

</body>
</html>
```